Post Card Design - For Financial

"9" length 6.5" height" post card of tallhedge.net trying to get people to text the word YES to our phone number to access our latest stock picks. or marketrove.io we own both of them. Call to action. Get winnin stock picks sign up now text the word "YES" to 888-312-4798. must haves: " track record 2023: 477.8%" "#1 stock picking newsletter in the U.S.A." " Disclaimer: The materials and content provided by TallHedge.net, including but not limited to our website, emails, blogs, and text messages (collectively, the "Materials"), are intended for general information purposes only and do not constitute financial, legal, or investment advice. TallHedge.net is engaged in the business of marketing and advertising companies for compensation. The information contained in the Materials is not, and should not be read as, an offer or recommendation to buy or sell any securities. All content is provided for informational and educational purposes only. TallHedge.net and its staff are not licensed investment advisors, brokers, or dealers. Any content provided by us is not intended to solicit or recommend any investment and should not be used as the basis for any investment decisions. We do not provide investment advice, endorse any financial product, or suggest that any particular investment or strategy is suitable for any specific person. TallHedge.net receives compensation from the companies featured in our alerts, emails, and other Materials for marketing and advertising services. The existence of such compensation may influence the content, topics, or posts made in the Materials. Investing in stocks, especially penny stocks, involves a high level of risk and may not be suitable for all investors. The possibility exists that you could sustain a loss of some or all of your initial investment. Therefore, you should not invest money that you cannot afford to lose. The performance figures stated in the Materials, including but not limited to a track record of 477% in 2023, are hypothetical and should not be considered indicative of future results. Past performance is not necessarily indicative of future results. Individual results may vary, and the examples used in the Materials are not guaranteed to occur. You are encouraged to perform your own due diligence and consult with a qualified financial advisor before making any investment decisions. TallHedge.net and its Materials should not be used as the sole basis for any investment decision. We make no representation or warranty as to the accuracy, completeness, or reliability of the information contained in the Materials. The content provided by TallHedge.net and in its newsletter is intended for entertainment purposes only. Acknowledgment: By using TallHedge.net's services, joining our site, or subscribing to our email/blog list, you acknowledge that you have read, understood, and agree to be bound by the terms of this disclaimer. If you do not agree with these terms, you should not use our services or subscribe to our Materials

."

Target Market(s)

investors

Industry/Entity Type

financial

Colors
0054AA
0677BA
7BADD7
CADEEF
E8F1F8
00AB8E
00BBA5
67D7C9
C6EFE9
E9F9F6
59FF00
82FF00
B8FF75
E3FFCB
F4FFEA

Requirements
Must have
• " track record 2023: 477.8%" "#1 stock picking newsletter in the U.S.A." "Disclaimer: The materials and content provided by TallHedge.net, including but not limited to our website, emails, blogs, and text messages (collectively, the "Materials"), are intended for general information purposes only and do not constitute financial, legal, or investment advice. TallHedge.net is engaged in the business of marketing and advertising companies for compensation. The information contained in the Materials is not, and should not be read as, an offer or recommendation to buy or sell any securities. All content is provided for informational and educational purposes only. TallHedge.net and its staff are not licensed investment advisors, brokers, or dealers. Any content provided by us is not intended to solicit or recommend any investment and should not be used as the basis for any investment decisions. We do not provide investment advice, endorse any financial product, or suggest that any particular investment or strategy is suitable for any specific person. TallHedge.net receives compensation from the companies featured in our alerts, emails, and other Materials for marketing and advertising services. The existence of such compensation may influence the content, topics, or posts made in the Materials. Investing in stocks, especially penny stocks, involves a high level of risk and may not be suitable for all investors. The possibility exists that you could sustain a loss of some or all of your initial investment. Therefore, you should not invest money that you cannot afford to lose. The performance figures stated in the Materials, including but not limited to a track record of 477% in 2023, are hypothetical and should not be considered indicative of future results. Past performance is not necessarily indicative of future results. Individual results may vary, and the examples used in the Materials are not guaranteed to occur. You are encouraged to perform your own due diligence and consult with a qualified financial advisor before making any investment decisions. TallHedge.net and its Materials should not be used as the sole basis for any investment decision. We make no representation or warranty as to the accuracy, completeness, or reliability of the information contained in the Materials. The content provided by TallHedge.net and in its newsletter is intended for entertainment purposes only. Acknowledgment: By using TallHedge.net's services, joining our site, or subscribing to our email/blog list, you acknowledge that you have read, understood, and agree to be bound by the terms of this disclaimer. If you do not agree with these terms, you should not use our services or subscribe to our Materials."
Nice to have
• call to action: Get exclusive stock picks delivered directly to your phone. Text "YES" to [888-312-4798] to receive your first stock pick

```html
<!DOCTYPE html>
<html lang="en">
<head>
<meta charset="UTF-8">
<title>TallHedge Postcard</title>
<link href="https://fonts.googleapis.com/css2?family=Jost:wght@400;500;600;700&display=swap" rel="stylesheet">
<style>
  :root {
    --page: #ffffff;
    --navy: #0a1a6e;
    --royal: #1c3bb8;
    --deep-blue: #0054aa;
    --mid-blue: #0677ba;
    --sky: #1aa3e8;
    --bubble: #2aa8ea;
    --ink: #111111;
    --white: #ffffff;
  }
  * { margin: 0; padding: 0; box-sizing: border-box; }
  html, body {
    width: 1200px;
    height: 1200px;
    overflow: hidden;
    background: var(--page);
    font-family: "Jost", "Futura", sans-serif;
  }
  .postcard {
    position: absolute;
    left: 200px;
    top: 45px;
    width: 800px;
    height: 1110px;
    background: var(--white);
    overflow: hidden;
  }
  .hero {
    position: absolute;
    left: 0; top: 0;
    width: 800px; height: 574px;
    background:
      radial-gradient(ellipse at 70% 40%, rgba(60,110,230,0.55), transparent 60%),
      linear-gradient(180deg, #1a2a9a 0%, #2440c0 45%, #13208a 80%, #0b1560 100%);
  }
  .headline {
    position: absolute;
    left: 0; top: 58px;
    width: 800px;
    text-align: center;
    color: var(--white);
    font-weight: 600;
    font-size: 41px;
    line-height: 1.15;
    letter-spacing: 0.5px;
    text-transform: uppercase;
  }
  .cta-bubble {
    position: absolute;
    left: 0; top: 0;
    width: 800px; height: 574px;
  }
  .cta-text {
    position: absolute;
    left: 230px; top: 300px;
    width: 350px;
    text-align: center;
    color: var(--white);
    font-size: 30px;
    line-height: 1.2;
    font-weight: 400;
    transform: rotate(-2deg);
  }
  .cta-text strong {
    font-weight: 700;
    font-size: 42px;
  }
  .accent-bar {
    position: absolute;
    left: 645px; top: 574px;
    width: 23px; height: 84px;
    background: var(--deep-blue);
  }
  .track-record {
    position: absolute;
    left: 45px; top: 606px;
  }
  .track-record h2 {
    font-size: 27px;
    font-weight: 600;
    color: var(--ink);
    line-height: 1.1;
  }
  .track-record p {
    font-size: 18px;
    color: var(--ink);
    line-height: 1.2;
  }
  .disclaimer {
    position: absolute;
    left: 45px; top: 690px;
    width: 712px;
    font-size: 14.6px;
    line-height: 1.22;
    color: var(--ink);
    text-align: justify;
  }
  .disclaimer strong { font-weight: 600; }
  .footer-bands {
    position: absolute;
    left: 0; bottom: 0;
    width: 800px; height: 50px;
  }
</style>
</head>
<body>
  <main class="postcard">
    <section class="hero" role="img" aria-label="Stock market ticker board with prices and charts in deep blue tones"></section>

    <h1 class="headline">Get exclusive stock picks<br>delivered directly<br>to your phone</h1>

    <svg class="cta-bubble" viewBox="0 0 800 574" aria-hidden="true">
      <g transform="rotate(-3 400 390)">
        <path d="M248 250 H520 L560 205 L552 250 H566 Q588 250 588 272 V520 Q588 542 566 542 H248 Q226 542 226 520 V272 Q226 250 248 250 Z"
              fill="var(--bubble)" />
      </g>
    </svg>
    <p class="cta-text">Text <strong>"YES"</strong><br>to [888-312-4798]<br>to receive<br>your first stock pick</p>

    <div class="accent-bar"></div>

    <section class="track-record">
      <h2>Track record 2023:</h2>
      <p>477.8%" "#1 stock picking newsletter in the U.S.A.</p>
    </section>

    <p class="disclaimer"><strong>Disclaimer:</strong> This report/release is a commercial advertisement and is for general information purposes ONLY. We are engaged in the business of marketing and advertising companies for compensation. Never invest in any stock featured on our site or emails unless you can afford to lose your entire investment. This disclaimer is to be read and fully understood before using our services, joining our site or our email/blog list. The track record, gains, upside, and/or losses mentioned are all hypothetical and should not be considered as the basis for investment. Penny-stock trading involves substantial risk, so always research every alert before trading, consult with a licensed professional before trading, only invest what you can afford to lose, and always trade with caution. Readers should independently investigate and fully understand all risks before investing. Results listed above are NOT typical and individual results may and most likely will vary. TallHedge and its staff are NOT licensed investment advisors or broker/dealers of any kind. Alerts are not a solicitation or recommendation to buy/sell/hold securities but merely investment ideas that should NEVER serve as the basis of your trading decisions. TallHedge and its newsletter are for entertainment purposes only. This website and its reports are for general information purposes as we are engaged in the business of marketing and advertising companies for monetary compensation. Any investment decision should be discussed with a financial adviser before taking place."</p>

    <svg class="footer-bands" viewBox="0 0 800 50" preserveAspectRatio="none" aria-hidden="true">
      <polygon points="0,50 0,32 40,18 175,18 150,50" fill="var(--deep-blue)" />
      <polygon points="130,50 175,18 380,18 390,8 800,8 800,50" fill="var(--sky)" />
      <polygon points="380,18 390,8 520,8 510,18" fill="var(--mid-blue)" />
    </svg>
  </main>
</body>
</html>
```